Simple Business Cards for Self-employed Coach

Simple business card with a design that includes the QLT logo.
Using either only the logo color or additional colors that match the logo.

Meridian Guides reach deeply into the past, gathering wisdom from East and West, while still staying current with the frontiers of new discovery in cognitive science, genetics, and other disciplines. see https://www.brightharborpath.example/what-is-integral-coaching/

Target Market(s)

Coaching Clients in Tokyo /Asia; in business organizations, but also outside

Industry/Entity Type

Life Coaching

Contact Information for Business Card

Lukas Brenning
Certified Meridian Guide

3-2-48 Kamiyoshi
Nakarino 164-0392
Tokyo, Japan

Phone: +81 70 4817 5062
E-Mail: lukas.brenning@mailora.example

Font styles to use
Sans Serif

Colors
00a990

Requirements
Must have
• include uploaded logo
• color fitting with QLT logo color
Nice to have
• simple, elegant design
Should not have
• clutter

```html
<!DOCTYPE html>
<html lang="en">
<head>
<meta charset="utf-8">
<title>QLT — Business Card</title>
<link rel="stylesheet" href="https://fonts.googleapis.com/css2?family=Oswald:wght@500;600&family=Open+Sans:wght@400;600;700&display=swap">
<style>
  :root {
    --stage: #1c1c1c;
    --card-dark: #2a2a2b;
    --card-dark-edge: #232324;
    --teal: #00a990;
    --teal-light: #0bb59b;
    --white: #ffffff;
    --text-soft: #d9d9d9;
    --icon: #00a990;
  }
  * { box-sizing: border-box; margin: 0; padding: 0; }
  html, body {
    width: 1200px; height: 1000px; overflow: hidden;
    background: var(--stage);
  }
  .card {
    position: absolute; left: 180px; top: 260px;
    width: 840px; height: 480px;
    border-radius: 36px; overflow: hidden;
    background: linear-gradient(135deg, var(--card-dark) 0%, var(--card-dark-edge) 100%);
    box-shadow: 0 18px 40px rgba(0,0,0,.45);
  }
  .brand-panel {
    position: absolute; left: 0; top: 0;
    width: 340px; height: 100%;
    background: linear-gradient(160deg, var(--teal-light) 0%, var(--teal) 100%);
  }
  .brand-notch {
    position: absolute; left: 340px; top: 118px;
    width: 0; height: 0;
    border-top: 14px solid transparent;
    border-bottom: 14px solid transparent;
    border-left: 16px solid var(--teal);
  }
  .brand-name {
    position: absolute; left: 0; top: 0; width: 340px; height: 100%;
    display: flex; align-items: center; justify-content: center; gap: 14px;
    padding-top: 70px;
    font-family: "Open Sans", sans-serif; font-weight: 700;
    font-size: 64px; letter-spacing: 8px; color: var(--white);
  }
  .brand-name .mark {
    width: 22px; height: 22px; background: var(--white);
  }
  .details {
    position: absolute; left: 400px; top: 72px; right: 40px;
    font-family: "Open Sans", sans-serif;
  }
  .person-name {
    font-family: "Oswald", sans-serif; font-weight: 600;
    font-size: 58px; line-height: 1; letter-spacing: 1px;
    text-transform: uppercase; color: var(--white);
  }
  .person-name .surname { color: var(--teal); }
  .person-title {
    margin-top: 8px; font-size: 22px; font-weight: 600; color: var(--white);
  }
  .address {
    margin-top: 58px; font-size: 18px; line-height: 1.35; color: var(--text-soft);
  }
  .contact-list { margin-top: 16px; list-style: none; }
  .contact-item {
    display: flex; align-items: center; gap: 18px;
    font-size: 18px; line-height: 1.55; color: var(--text-soft);
  }
  .contact-item svg { width: 20px; height: 20px; flex: none; }
  .contact-item .accent { color: var(--teal); }
</style>
</head>
<body>
  <div class="card">
    <div class="brand-panel"></div>
    <div class="brand-notch"></div>
    <div class="brand-name"><span class="mark"></span>QLT</div>

    <div class="details">
      <h1 class="person-name">Daniel <span class="surname">Orwick</span></h1>
      <p class="person-title">Certified Meridian Guide</p>

      <p class="address">3-2-48 Kamiyoshi Nakarino<br>164-0392 Tokyo,Japan</p>

      <ul class="contact-list">
        <li class="contact-item">
          <svg viewBox="0 0 20 20" fill="none" stroke="var(--icon)" stroke-width="1.4"><rect x="6" y="2" width="8" height="16" rx="1.5"/><line x1="9" y1="15.5" x2="11" y2="15.5"/></svg>
          +81 70 4817 5062
        </li>
        <li class="contact-item">
          <svg viewBox="0 0 20 20" fill="none" stroke="var(--icon)" stroke-width="1.4"><rect x="2" y="5" width="16" height="11"/><polyline points="2,5 10,11 18,5"/></svg>
          lukas.brenning@mailora.example
        </li>
        <li class="contact-item">
          <svg viewBox="0 0 20 20" fill="none" stroke="var(--icon)" stroke-width="1.4"><circle cx="10" cy="10" r="8"/><ellipse cx="10" cy="10" rx="3.5" ry="8"/><line x1="2" y1="10" x2="18" y2="10"/></svg>
          <span>www.<span class="accent">brightharborpath</span>.example</span>
        </li>
      </ul>
    </div>
  </div>
</body>
</html>
```